Fernbrook Plots - Online-only garden installation company

Online-only garden installation company. Our demographic is middle aged / suburban women, and we anticipate Facebook driving traffic to this website, as well as referrals from garden centers. The website must be very simple in design and function.

All orders will be placed through the website, including size of garden (3 options), location in yard, payment, and scheduling of installation date.

The website should employ a 3 step process:

Step 1: Select garden size. Either an 4' X 4', 8' X 4', or 12' X 4'.

Step 2: Select a location. We would like to use MapFinder to look up a US address, then "drag and drop" one of the garden sizes from step 1 to the location the customer would like us to install the garden at their home.

Step 3: Pick an installation date and pay. Using an online calendar the customer will pick a date, and then pay for the installation via credit card.

The website will be linked to an email account, FernbrookPlots@mailzy.com to inform us of orders placed.

Target Market(s)

Our demographic is middle aged / suburban women, and we anticipate Facebook driving traffic to this website, as well as referrals from garden centers.

Industry/Entity Type

Coding

Number of Pages Required

Requirements
Must have
• Scheduling and payment options.

```html
<!DOCTYPE html>
<html lang="en">
<head>
<meta charset="utf-8">
<title>Fernbrook Plots – Garden Installation Company</title>
<link href="https://fonts.googleapis.com/css2?family=Open+Sans:ital,wght@0,400;0,600;0,700;0,800;1,400&display=swap" rel="stylesheet">
<style>
:root{
  --green:#3a7a35;
  --green-dark:#2f6a2b;
  --green-soft:#e8f2e6;
  --orange:#e0582a;
  --yellow:#f4d23c;
  --text:#555;
  --text-dark:#333;
  --line:#ddd;
  --panel:#f4f4f4;
  --band:#333;
  --footer:#f3f3f3;
  --white:#fff;
}
*{box-sizing:border-box;margin:0;padding:0}
html,body{width:1200px;height:2817px;overflow:hidden}
body{font-family:"Open Sans",Arial,sans-serif;color:var(--text);background:var(--white);position:relative}
.abs{position:absolute}
.btn{position:absolute;background:var(--orange);color:var(--white);font-weight:700;text-transform:uppercase;display:flex;align-items:center;justify-content:center;letter-spacing:.5px}
.heading{position:absolute;color:var(--green);font-weight:700;text-transform:uppercase;font-size:26px;letter-spacing:.5px}

/* header */
.brand{left:75px;top:40px;display:flex;align-items:center;gap:10px}
.brand-dot{width:22px;height:22px;border-radius:50%;background:var(--orange)}
.brand-name{font-weight:800;color:var(--green-dark);font-size:19px;line-height:1.05;text-transform:uppercase;width:120px}
.phone{left:588px;top:34px;color:var(--orange);font-weight:600;font-size:17px;display:flex;align-items:center;gap:8px}
.search{left:753px;top:24px;width:270px;height:44px;border:1px solid #ccc;border-radius:3px;display:flex;align-items:center;justify-content:space-between;padding:0 12px;font-size:14px;color:#888}
.login{left:1037px;top:26px;width:90px;height:40px;font-size:13px;border-radius:2px}
.nav{right:73px;top:110px;display:flex;gap:37px;font-size:12.5px;font-weight:700;text-transform:uppercase;color:var(--text-dark)}
.nav .active{color:var(--green)}

/* hero */
.hero{left:0;top:160px;width:1200px;height:499px;background:linear-gradient(100deg,#6c5a44 0%,#7d7660 30%,#5d7a3b 55%,#4f6a33 75%,#6b5236 100%)}
.hero-title{left:73px;top:368px;color:var(--white);font-weight:800;font-size:38px;letter-spacing:1.5px}
.hero-sub{left:74px;top:416px;color:var(--white);font-weight:700;font-size:25px;letter-spacing:.5px}
.dots{left:75px;top:481px;display:flex;gap:6px}
.dots span{width:13px;height:13px;border-radius:50%;background:var(--white)}
.dots span:first-child{background:var(--orange)}
.order{left:793px;top:229px;width:334px;height:366px;background:var(--white)}
.order-head{height:53px;background:var(--green);color:var(--white);font-weight:700;font-size:25px;padding:10px 20px;letter-spacing:.5px}
.field{position:absolute;left:20px;width:291px;height:41px;border:1px solid #ccc;border-radius:2px;font-size:13px;color:#555;display:flex;align-items:center;justify-content:space-between;padding:0 12px}
.submit{left:20px;top:293px;width:291px;height:51px;font-size:19px;border-radius:3px}

/* welcome */
.welcome-text{left:75px;top:758px;width:690px;font-size:15.5px;line-height:27px}
.welcome-text p{margin-bottom:7px}
.read-more{left:75px;top:1008px;width:165px;height:46px;font-size:13px}
.reviews{left:793px;top:710px;width:334px;height:344px;background:var(--panel);padding:18px 20px}
.reviews h2{color:var(--green);font-size:26px;font-weight:700}
.arrows{position:absolute;right:22px;top:24px;display:flex;gap:12px}
.quote{margin-top:22px;font-style:italic;font-size:14.5px;line-height:28px;color:#555}
.reviewer{position:absolute;left:20px;top:230px;display:flex;align-items:center;gap:20px}
.avatar{width:84px;height:84px;border-radius:50%;background:radial-gradient(circle,#d6b07c,#7fa25a);border:3px solid var(--white)}
.reviewer b{display:block;color:var(--orange);font-size:14px;font-weight:700}
.reviewer small{font-size:11px;font-weight:700;color:#777;letter-spacing:.5px}

/* process */
.process{left:0;top:1097px;width:1200px;height:477px;background:linear-gradient(90deg,var(--green) 0%,var(--green) 44%,#4e8a36 58%,#6e9a3e 72%,#8a6a3c 85%,#5c7a32 100%)}
.process-title{left:75px;top:1140px;color:var(--white);font-size:28px;font-weight:700;text-transform:uppercase}
.process-title em{font-style:normal;color:var(--yellow)}
.step{position:absolute;left:75px;width:690px;display:flex;gap:24px;color:var(--white)}
.step-icon{flex:none;width:66px;height:66px;border:2px solid var(--white);border-radius:50%;display:flex;align-items:center;justify-content:center}
.step-label{color:var(--yellow);font-weight:700;font-size:17px;margin-bottom:4px}
.step p{font-size:14.5px;line-height:25px}
.step p b{font-weight:700}

/* gallery */
.gallery-title{left:0;width:1200px;top:1612px;text-align:center}
.photo{position:absolute}

.divider{left:75px;top:2162px;width:1052px;height:1px;background:var(--line)}

/* calendar */
.calendar{left:75px;top:2240px;width:361px;height:277px;background:#f3f6f3;border-top:3px solid var(--green);padding:10px 12px}
.cal-top{display:flex;justify-content:space-between;align-items:center;font-size:9px;font-weight:700;color:#555;padding:4px 6px 8px}
.cal-top b{font-size:12px;text-align:center;color:var(--text-dark);line-height:1.1}
.cal-grid{display:grid;grid-template-columns:repeat(7,1fr);border-left:1px solid var(--line);border-top:1px solid var(--line);background:var(--white)}
.cal-grid div{height:37px;border-right:1px solid var(--line);border-bottom:1px solid var(--line);display:flex;align-items:center;justify-content:center;font-size:11px;color:var(--green);text-decoration:underline}
.cal-grid .dow{height:22px;background:var(--green-soft);font-size:9px;font-weight:700;text-decoration:none;color:var(--green)}
.cal-grid .today{background:var(--green);color:var(--white)}

/* blog */
.blog-title{left:823px;top:2234px;width:304px;color:var(--green);font-weight:700;font-size:14px;line-height:22px;text-transform:uppercase}
.blog-text{left:823px;top:2292px;width:304px;font-size:15px;line-height:27px}
.blog-more{left:826px;top:2455px;width:149px;height:45px;font-size:13px}

/* newsletter */
.newsletter{left:0;top:2562px;width:1200px;height:78px;background:var(--band)}
.news-title{left:192px;top:2582px;color:var(--white);font-size:27px;font-weight:700;letter-spacing:.5px}
.news-input{left:522px;top:2579px;width:325px;height:45px;background:var(--white);font-size:12px;color:#777;display:flex;align-items:center;padding:0 14px}
.subscribe{left:860px;top:2579px;width:147px;height:45px;font-size:14px}

/* footer */
.footer{left:0;top:2640px;width:1200px;height:177px;background:var(--footer)}
.copyright{left:75px;top:2693px;font-size:12px;color:#777}
.social{left:75px;top:2732px;display:flex;gap:16px}
.social span{width:16px;height:16px;border-radius:50%;background:var(--text-dark)}
.accepted{left:909px;top:2691px;color:var(--green);font-weight:700;font-size:13px;text-transform:uppercase}
.cards{left:909px;top:2730px;display:flex;gap:18px}
.cards span{width:41px;height:26px;border-radius:4px;background:#999}
</style>
</head>
<body>

<!-- header -->
<div class="abs brand"><span class="brand-dot"></span><span class="brand-name">Fernbrook Plots</span></div>
<div class="abs phone">
  <svg width="15" height="15" viewBox="0 0 24 24"><path fill="#e0582a" d="M6.6 10.8a15.1 15.1 0 0 0 6.6 6.6l2.2-2.2c.3-.3.7-.4 1-.2 1.1.4 2.3.6 3.6.6.6 0 1 .4 1 1V20c0 .6-.4 1-1 1A17 17 0 0 1 3 4c0-.6.4-1 1-1h3.5c.6 0 1 .4 1 1 0 1.3.2 2.5.6 3.6.1.3 0 .7-.2 1z"/></svg>
  1-800-555-0142
</div>
<div class="abs search"><span>Search...</span>
  <svg width="17" height="17" viewBox="0 0 24 24"><circle cx="10" cy="10" r="7" fill="none" stroke="#333" stroke-width="3"/><path d="M15 15l6 6" stroke="#333" stroke-width="3"/></svg>
</div>
<div class="btn login">Log In</div>
<nav class="abs nav">
  <span class="active">Home</span><span>About Us</span><span>Services</span><span>Order Process</span><span>Gallery</span><span>Blog</span><span>Reviews</span><span>Contact Us</span>
</nav>

<!-- hero -->
<div class="abs hero" role="img" aria-label="Garden tools, watering can and seedlings on a wooden table"></div>
<h1 class="abs hero-title">FERNBROOK PLOTS</h1>
<div class="abs hero-sub">Garden Installation Company</div>
<div class="abs dots"><span></span><span></span><span></span><span></span></div>

<form class="abs order">
  <div class="order-head">QUICK ORDER</div>
  <div class="field" style="top:79px">Size of Garden
    <svg width="10" height="10" viewBox="0 0 10 10"><path d="M2 3l3 3 3-3" fill="none" stroke="#555" stroke-width="1.5"/></svg></div>
  <div class="field" style="top:133px">Location in Yard
    <svg width="11" height="13" viewBox="0 0 24 24"><path fill="#555" d="M12 2a7 7 0 0 0-7 7c0 5 7 13 7 13s7-8 7-13a7 7 0 0 0-7-7zm0 9.5A2.5 2.5 0 1 1 12 6.5a2.5 2.5 0 0 1 0 5z"/></svg></div>
  <div class="field" style="top:188px">Payment Mode
    <svg width="14" height="11" viewBox="0 0 24 18"><rect x="1" y="1" width="22" height="16" rx="2" fill="none" stroke="#555" stroke-width="2"/><rect x="1" y="5" width="22" height="3" fill="#555"/></svg></div>
  <div class="field" style="top:241px">Installation Date
    <svg width="12" height="12" viewBox="0 0 24 24"><rect x="2" y="4" width="20" height="18" rx="2" fill="none" stroke="#555" stroke-width="2.5"/><path d="M2 9h20M7 1v5M17 1v5" stroke="#555" stroke-width="2.5"/></svg></div>
  <div class="btn submit">Submit</div>
</form>

<!-- welcome -->
<h2 class="heading" style="left:75px;top:702px">Welcome to Our Website</h2>
<div class="abs welcome-text">
  <p>Aliquam molestie, mi et imperdiet euismod, dui purus auctor tellus, et interdum lacus lectus et ante. Sed accumsan sollicitudin sapien, sit amet adipiscing turpis gravida ac. In congue, neque ac lobortis volutpat, libero mauris varius mi, vitae suscipit ipsum ligula vitae risus. Duis aliquam nibh a dui iaculis viverra id a velit. Vivamus egestas risus in magna varius commodo. Sed semper viverra egestas. Etiam pretium porttitor lectus, vel ornare neque porta volutpat.</p>
  <p>Vestibulum dolor nulla, ultrices ac tincidunt sed, laoreet non est. Suspendisse lobortis turpis in odio blandit ac interdum lorem euismod. Etiam risus massa, vulputate eu pellentesque et, consectetur a neque.</p>
</div>
<div class="btn read-more">Read More</div>

<aside class="abs reviews">
  <h2>REVIEWS</h2>
  <div class="arrows">
    <svg width="12" height="20" viewBox="0 0 12 20"><path d="M10 2L3 10l7 8" fill="none" stroke="#666" stroke-width="3"/></svg>
    <svg width="12" height="20" viewBox="0 0 12 20"><path d="M2 2l7 8-7 8" fill="none" stroke="#e0582a" stroke-width="3"/></svg>
  </div>
  <p class="quote">“ Aliquam molestie, mi et imperdiet euismod, dui purus auctor tellus, et interdum lacus lectus et ante. Sed accumsan sollicitudin sapien, sit amet adipiscing turpis gravida ac...”</p>
  <div class="reviewer">
    <div class="avatar" role="img" aria-label="Customer portrait"></div>
    <div><b>NAME HEADING</b><small>LOCATION</small></div>
  </div>
</aside>

<!-- order process -->
<section class="abs process" role="img" aria-label="Gardener in a cap and overalls kneeling among green plants"></section>
<h2 class="abs process-title">Order Process in <em>3 Easy Steps</em></h2>

<div class="step" style="top:1203px">
  <div class="step-icon"><svg width="28" height="28" viewBox="0 0 24 24" fill="none" stroke="#fff" stroke-width="2.4"><path d="M3 3l7 7M3 3h6M3 3v6M21 3l-7 7M21 3h-6M21 3v6M3 21l7-7M3 21h6M3 21v-6M21 21l-7-7M21 21h-6M21 21v-6"/></svg></div>
  <div><div class="step-label">Step 1:</div><p><b>Select garden size.</b> Either an 4' X 4', 8' X 4', or 12' X 4'.</p></div>
</div>
<div class="step" style="top:1297px">
  <div class="step-icon"><svg width="22" height="28" viewBox="0 0 24 30" fill="none" stroke="#fff" stroke-width="2.4"><path d="M12 2a9 9 0 0 0-9 9c0 7 9 17 9 17s9-10 9-17a9 9 0 0 0-9-9z"/><circle cx="12" cy="11" r="3"/></svg></div>
  <div><div class="step-label">Step 2:</div><p><b>Select a location.</b> We would like to use MapFinder to look up a US address, then “drag and drop” one of the garden sizes from step 1 to the location the customer would like us to install the garden at their home.</p></div>
</div>
<div class="step" style="top:1443px">
  <div class="step-icon"><svg width="28" height="28" viewBox="0 0 24 24" fill="none" stroke="#fff" stroke-width="2"><rect x="2" y="4" width="20" height="18" rx="2"/><path d="M2 9h20M7 1v5M17 1v5M6 13h2M11 13h2M16 13h2M6 17h2M11 17h2M16 17h2"/></svg></div>
  <div><div class="step-label">Step 3:</div><p><b>Pick an installation date and pay.</b> Using an online calendar the customer will pick a date, and then pay for the installation via credit card.</p></div>
</div>

<!-- gallery -->
<h2 class="heading gallery-title">Photo Gallery</h2>
<div class="photo" style="left:75px;top:1683px;width:423px;height:422px;background:linear-gradient(160deg,#7aa03e,#4a6a2c 60%,#5a4632)" role="img" aria-label="Smiling couple kneeling in a garden bed"></div>
<div class="photo" style="left:511px;top:1683px;width:255px;height:203px;background:linear-gradient(150deg,#6d9a3a,#4b3b2a)" role="img" aria-label="Hands planting a seedling in soil"></div>
<div class="photo" style="left:779px;top:1683px;width:348px;height:203px;background:linear-gradient(150deg,#5d7a3a,#a05e4a 50%,#3e5a2a)" role="img" aria-label="Gardener tending flowers"></div>
<div class="photo" style="left:511px;top:1900px;width:255px;height:205px;background:linear-gradient(150deg,#d6c24a,#6a8a3a 60%,#3e5a2a)" role="img" aria-label="Gardener in orange cap among yellow flowers"></div>
<div class="photo" style="left:779px;top:1900px;width:348px;height:205px;background:linear-gradient(150deg,#4a7a30,#7aa848 50%,#c04a6a)" role="img" aria-label="Landscaped garden with a winding path"></div>

<div class="abs divider"></div>

<!-- calendar -->
<h2 class="heading" style="left:75px;top:2183px">Calender</h2>
<div class="abs calendar">
  <div class="cal-top"><span>PREV</span><b>JANUARY<br>2017</b><span>NEXT</span></div>
  <div class="cal-grid">
    <div class="dow">MON</div><div class="dow">TUE</div><div class="dow">WED</div><div class="dow">THU</div><div class="dow">FRI</div><div class="dow">SAT</div><div class="dow">SUN</div>
    <div>28</div><div>29</div><div>30</div><div>31</div><div>1</div><div>2</div><div>3</div>
    <div>5</div><div>6</div><div>7</div><div>8</div><div>9</div><div>10</div><div>11</div>
    <div>12</div><div>13</div><div>14</div><div>15</div><div>16</div><div>17</div><div>18</div>
    <div>19</div><div>20</div><div>21</div><div>22</div><div>23</div><div>24</div><div>25</div>
    <div>26</div><div>27</div><div>28</div><div>29</div><div class="today">30</div><div>31</div><div>1</div>
  </div>
</div>

<!-- blog -->
<h2 class="heading" style="left:524px;top:2183px">Blog Posts</h2>
<div class="photo" style="left:524px;top:2240px;width:270px;height:277px;background:linear-gradient(150deg,#c06a8a,#5a8a3a 45%,#3e6a2a 70%,#8a7ab0)" role="img" aria-label="Flower garden with a curved lawn path"></div>
<h3 class="abs blog-title">Aliquam molestie, mi et imperdiet euismod dui purus aucto</h3>
<p class="abs blog-text">Sed accumsan sollicitudin sapien, sit amet adipiscing turpis gravida ac. In congue, neque ac lobortis volutpat, libero mauris varius mi, vitae suscipit ipsum ligula vitae risus.</p>
<div class="btn blog-more">Read More</div>

<!-- newsletter -->
<div class="abs newsletter"></div>
<h2 class="abs news-title">NEWSLETTER SIGN UP</h2>
<div class="abs news-input">Enter Email Address</div>
<div class="btn subscribe">Subscribe</div>

<!-- footer -->
<footer class="abs footer"></footer>
<div class="abs copyright">Copyright © 2017. Company Name. All Right Reserved</div>
<div class="abs social"><span></span><span></span><span></span><span></span><span></span><span></span></div>
<div class="abs accepted">We Accepted</div>
<div class="abs cards"><span></span><span></span><span></span><span></span></div>

</body>
</html>
```